Managed Service Provider need new business cards

We are a small Maanged Service Provider of IT Services and need a new fresh design for our business cards. We want something impossible, fun and professional :)
Our services has a large range, but we are always fun and make sure our customers both get their issue sorted and also feel like they are "catching up with an old friend".
All our cards in the past has always been all black, with red and we need something fresher.
The back of card, we would like just a small list of what we do i think, but if someone has a better idea, please do something cool with the back of the card:
Managed IT Services
Productivity Solutions
Data Backup and Recovery
IT System Maintenance
Managed IT Security
More details can be found on our website tqnetworks.com.au
Industry/Entity Type
It Company
Contact Information for Business Card
Name: Dwayne Falstrup
Title: Director
Phone: 03 6193 4827
Mobile: 0412 587 239
Email: dwayne@tqnetworks.com.au
Web: www.tqnetworks.com.au

```html
<!DOCTYPE html>
<html lang="en">
<head>
<meta charset="utf-8">
<title>TQ Networks – Business Cards</title>
<link rel="stylesheet" href="https://fonts.googleapis.com/css2?family=Oswald:wght@500;700&family=Roboto:wght@400;500&display=swap">
<style>
  :root {
    --red: #d3242b;
    --black: #0d0d0d;
    --charcoal: #1b1b1b;
    --faint: #232323;
    --white: #ffffff;
    --paper: #e9e6e1;
    --mouse-tone: #d9d9d9;
    --text-dark: #222222;
  }
  * { box-sizing: border-box; margin: 0; padding: 0; }
  html, body {
    width: 900px; height: 1200px; overflow: hidden;
    background: var(--paper);
  }
  .canvas { position: relative; width: 900px; height: 1200px; }
  .card {
    position: absolute; left: 60px; width: 780px; height: 450px;
    border-radius: 22px; overflow: hidden;
    box-shadow: 0 6px 18px rgba(0,0,0,.25);
  }
  .card--front { top: 120px; background: var(--white); }
  .card--back {
    top: 630px;
    background: linear-gradient(160deg, #262626 0%, var(--black) 70%);
  }
  .card__art { position: absolute; inset: 0; }

  .brand-name {
    position: absolute; font-family: "Oswald", sans-serif; font-weight: 700;
    letter-spacing: 1px; line-height: 1; text-transform: uppercase;
  }
  .card--front .brand-name { left: 34px; top: 34px; font-size: 50px; color: var(--red); }

  .person { position: absolute; right: 0; top: 46px; text-align: right; }
  .person__name {
    display: inline-block; background: var(--red); color: var(--white);
    font-family: "Oswald", sans-serif; font-weight: 500; font-size: 24px;
    padding: 4px 34px 4px 28px; text-transform: uppercase; letter-spacing: .5px;
  }
  .person__title {
    font-family: "Roboto", sans-serif; font-size: 17px; color: var(--text-dark);
    padding-right: 34px; margin-top: 4px;
  }

  .contacts {
    position: absolute; right: 34px; bottom: 30px; color: var(--white);
    font-family: "Roboto", sans-serif; font-size: 17px;
  }
  .contacts__row { display: flex; justify-content: flex-end; gap: 22px; margin-top: 12px; }
  .contact { display: flex; align-items: center; gap: 7px; }
  .contact svg { width: 16px; height: 16px; fill: var(--white); }

  .card--back .watermark-letters {
    position: absolute; left: 230px; top: -30px; font-family: "Oswald", sans-serif;
    font-weight: 700; font-size: 330px; color: var(--faint); line-height: 1;
  }
  .card--back .brand-name {
    left: 0; right: 0; top: 92px; text-align: center; font-size: 76px; color: var(--white);
  }
  .card--back .mouse-art {
    position: absolute; left: 345px; top: 192px; width: 90px; height: 110px;
  }
  .services {
    position: absolute; left: 40px; right: 40px; bottom: 40px; text-align: center;
    font-family: "Roboto", sans-serif; font-weight: 500; font-size: 17px;
    color: var(--white); text-transform: uppercase; line-height: 1.5; letter-spacing: .3px;
  }
</style>
</head>
<body>
<main class="canvas">

  <section class="card card--front" aria-label="Business card front">
    <svg class="card__art" viewBox="0 0 780 450" aria-hidden="true">
      <path d="M60 200 C200 130 300 235 420 200 C560 165 640 110 780 100 L780 150 C600 170 520 230 380 280 C250 330 150 260 0 300 L0 240 C20 225 40 210 60 200 Z" fill="var(--red)"/>
      <path d="M0 300 C150 260 250 330 380 280 C520 230 600 170 780 150 L780 450 L0 450 Z" fill="var(--black)"/>
    </svg>
    <svg class="card__art" viewBox="0 0 780 450">
      <g role="img" aria-label="Illustration of a computer mouse with its cable">
        <ellipse cx="130" cy="340" rx="110" ry="68" transform="rotate(-18 130 340)" fill="var(--mouse-tone)"/>
      </g>
    </svg>

    <div class="brand-name">TQ Networks</div>

    <div class="person">
      <div class="person__name">Dwayne Falstrup</div>
      <div class="person__title">Director</div>
    </div>

    <div class="contacts">
      <div class="contacts__row">
        <span class="contact">
          <svg viewBox="0 0 16 16"><path d="M3 1h3l1.5 4-2 1.2a9 9 0 0 0 4.3 4.3L11 8.5l4 1.5v3a2 2 0 0 1-2 2A12 12 0 0 1 1 3a2 2 0 0 1 2-2z"/></svg>
          03 6193 4827
        </span>
        <span class="contact">
          <svg viewBox="0 0 16 16"><path d="M4.5 0h7A1.5 1.5 0 0 1 13 1.5v13a1.5 1.5 0 0 1-1.5 1.5h-7A1.5 1.5 0 0 1 3 14.5v-13A1.5 1.5 0 0 1 4.5 0zM5 2v10h6V2zm3 11a1 1 0 1 0 0 2 1 1 0 0 0 0-2z"/></svg>
          0412 587 239
        </span>
      </div>
      <div class="contacts__row">
        <span class="contact">
          <svg viewBox="0 0 16 16"><path d="M1 3h14v10H1zm1.5 1.5v.4L8 8.6l5.5-3.7v-.4zm0 2.2v4.8h11V6.7L8 10.4z"/></svg>
          dwayne@tqnetworks.com.au
        </span>
        <span class="contact">
          <svg viewBox="0 0 16 16"><path d="M8 0a8 8 0 1 0 0 16A8 8 0 0 0 8 0zm5.9 7h-2.5a12 12 0 0 0-1.2-4.9A6 6 0 0 1 13.9 7zM8 2c.8 1 1.4 2.8 1.5 5h-3C6.6 4.8 7.2 3 8 2zM5.8 2.1A12 12 0 0 0 4.6 7H2.1a6 6 0 0 1 3.7-4.9zM2.1 9h2.5a12 12 0 0 0 1.2 4.9A6 6 0 0 1 2.1 9zM8 14c-.8-1-1.4-2.8-1.5-5h3c-.1 2.2-.7 4-1.5 5zm2.2-.1A12 12 0 0 0 11.4 9h2.5a6 6 0 0 1-3.7 4.9z"/></svg>
          www.tqnetworks.com.au
        </span>
      </div>
    </div>
  </section>

  <section class="card card--back" aria-label="Business card back">
    <div class="watermark-letters" aria-hidden="true">TQ</div>
    <div class="brand-name">TQ Networks</div>
    <svg class="mouse-art" viewBox="0 0 90 110">
      <g role="img" aria-label="Line illustration of a computer mouse">
        <ellipse cx="45" cy="60" rx="34" ry="46" fill="var(--mouse-tone)"/>
      </g>
    </svg>
    <div class="services">
      Managed IT Services • Productivity Solutions • Data Backup and Recovery<br>
      IT System Maintenance • Managed IT Security
    </div>
  </section>

</main>
</body>
</html>
```